Business Card Design Project

Vexolyte will provide 3D analysis of remote sensing digital data sets of airborne (aircraft/UAV) and satellite data in order to deliver 3D geospatial mapping information, videos and augmented reality products. Typical high end customers are military and security related customers, line object infrastructure owners or providers (pipelines gas/oil/fuel/water, energy lines, borders, coastal zones and rivers, transportation roads on the sea, roads, and railway systems). All these potential customers are linked to regular service monitoring, surveillance and reconnaissance covering cities, counties and countries. The company will provide 3D presentation of infrastructure (which is likely to become a binding requirement in Europe and other countries), disaster prevention and monitoring.

Target Market(s)

Target market are US based governmental agencies, such as Bureau of Civic Safeguards, Federal Terrasight bureau, Ministery of Garrison Affairs, Office of Landholdings/Federal Strata Bureau, etc as well as commercial entities like gas, utilities, etc > Primary services will be to provide 3D geospatial mapping to support search & rescue, border control, infrastructure (pipeline, electric wires, etc.) management, agriculture, climate control, etc.

Industry/Entity Type

Business

Contact Information for Business Card

Vincent Renz6 Gristmill RdCedar Knolls, NJ 079271-973-652-8379vrenz.straight4ward@gmail.com

Requirements
Must have
• Business card must have the company logo (provided) - and want to keep with the colors in the logo

```html
<!DOCTYPE html>
<html lang="en">
<head>
<meta charset="utf-8">
<title>Vexolyte – Business Card</title>
<link href="https://fonts.googleapis.com/css2?family=Lato:wght@300;400;700&display=swap" rel="stylesheet">
<style>
  :root {
    --backdrop: #e9e9e9;
    --card: #fbfbfb;
    --card-edge: #dedede;
    --brand-red: #d8182c;
    --brand-navy: #1d4658;
    --ink: #222a2e;
    --rule: #e4637a;
  }
  * { margin: 0; padding: 0; box-sizing: border-box; }
  html, body {
    width: 1200px;
    height: 900px;
    overflow: hidden;
    background: var(--backdrop);
    font-family: "Lato", sans-serif;
  }
  .business-card {
    position: absolute;
    left: 150px;
    top: 175px;
    width: 900px;
    height: 550px;
    background: var(--card);
    border: 2px solid var(--card-edge);
    border-radius: 24px;
    box-shadow: 0 10px 30px rgba(0,0,0,0.08);
  }
  .brand {
    position: absolute;
    top: 88px;
    left: 0;
    right: 0;
    display: flex;
    justify-content: center;
    align-items: center;
    gap: 22px;
  }
  .brand-square {
    width: 34px;
    height: 34px;
    background: var(--brand-red);
  }
  .brand-name {
    font-weight: 300;
    font-size: 92px;
    line-height: 1;
    letter-spacing: 2px;
    color: var(--brand-navy);
  }
  .name-row {
    position: absolute;
    top: 300px;
    left: 0;
    right: 0;
    display: flex;
    align-items: center;
  }
  .name-row .rule {
    flex: 1;
    height: 1.5px;
    background: var(--rule);
  }
  .holder-name {
    padding: 0 16px;
    font-weight: 700;
    font-size: 31px;
    letter-spacing: 0.5px;
    color: var(--brand-red);
    text-transform: uppercase;
  }
  .contact {
    position: absolute;
    top: 375px;
    left: 0;
    right: 0;
    text-align: center;
    color: var(--ink);
    font-size: 23px;
  }
  .contact-line {
    display: flex;
    justify-content: center;
    align-items: center;
    gap: 4px;
    height: 38px;
  }
  .contact-line svg { width: 18px; height: 18px; fill: var(--brand-red); }
  .contact-line.address { margin-top: 18px; }
</style>
</head>
<body>
  <div class="business-card">
    <div class="brand">
      <span class="brand-square"></span>
      <span class="brand-name">Vexolyte</span>
    </div>

    <div class="name-row">
      <span class="rule"></span>
      <span class="holder-name">Harold Brisk</span>
      <span class="rule"></span>
    </div>

    <div class="contact">
      <div class="contact-line phone">
        <svg viewBox="0 0 24 24" aria-hidden="true"><path d="M3 9c0-3 4-5 9-5s9 2 9 5v2h-5V9c-1-.6-2.5-1-4-1s-3 .4-4 1v2H3z M6 12h12l2 8H4z"/></svg>
        <span>1-555-218-4093</span>
      </div>
      <div class="contact-line email">
        <svg viewBox="0 0 24 24" aria-hidden="true"><path d="M2 5h20v14H2z M4 7v.5l8 5.5 8-5.5V7z" fill-rule="evenodd"/></svg>
        <span>hbrisk.onpath22@mailcove.example</span>
      </div>
      <div class="contact-line address">
        <span>41 Pelham LnMaple Hollow, NJ 08314</span>
      </div>
    </div>
  </div>
</body>
</html>
```